Koru upkeep TV Solar Solution

Solar power system install
Services and maintenance
wiring, Rewinding and Renovation
Switch Board Upgrade
Power and lighting point
t doesn’t matter how much you spend on quality parts, your solar system will let you down if your design and installation are sub-par. Have your solar system tailored and installed by our Master Electrician and Bright Grid Guild Accredited team.

Target Market(s)

sales and installed

Industry/Entity Type

Solar install and retailer

Contact Information for Business Card

Name , Email, Phone Number ,Business address,

Font styles to use
Serif

Colors
0054AA
0677BA
7BADD7
CADEEF
E8F1F8

Requirements
Must have
• clear and bright
Nice to have
• new design
Should not have
• unclear pictures

```html
<!DOCTYPE html>
<html lang="en">
<head>
<meta charset="utf-8">
<title>TV Solar Solution – Business Card</title>
<link rel="stylesheet" href="https://fonts.googleapis.com/css2?family=Poppins:wght@400;500;600;700&family=Roboto+Condensed:ital,wght@1,700;1,800&family=Noto+Serif:ital@1&display=swap">
<style>
:root{
  --page:#053a7e;
  --header:#00964a;
  --header-text:#eef2e6;
  --card-light:#eef4fb;
  --brand-deep:#1f4a9c;
  --brand-mid:#2a7cc4;
  --brand-bright:#0677ba;
  --ink:#1c1c1c;
  --ink-name:#2f4a78;
  --quote:#2a5fb0;
  --white:#ffffff;
  --edge:#c9d3e0;
}
*{margin:0;padding:0;box-sizing:border-box}
html,body{width:1200px;height:1200px;overflow:hidden}
body{background:var(--page);position:relative;font-family:"Poppins",sans-serif}

.header-band{position:absolute;left:0;top:0;width:1200px;height:144px;background:var(--header);
  color:var(--header-text);text-align:center;font-weight:600;font-size:30px;line-height:44px;padding-top:29px}

.card{position:absolute;left:258px;width:724px;height:415px;border-radius:24px;overflow:hidden;
  border:2px solid var(--edge)}
.card-front{top:208px;background:linear-gradient(135deg,#f3f7fc,var(--card-light))}
.card-back{top:686px;background:var(--white)}

.front-art{position:absolute;left:0;top:0}
.holder-name{position:absolute;left:44px;top:36px;font-size:38px;color:var(--ink-name);font-weight:400;letter-spacing:.2px}
.holder-role{position:absolute;left:44px;top:94px;font-size:16px;color:var(--ink);font-weight:500}
.holder-name strong{font-weight:600}

.contact-list{position:absolute;left:44px;top:180px;list-style:none}
.contact-list li{display:flex;align-items:center;height:37px;font-size:19px;color:var(--ink);font-weight:500}
.contact-icon{width:22px;height:22px;margin-right:14px;flex:none}

.brand-banner{position:absolute;left:0;top:316px;width:368px;height:66px;border-radius:0 33px 33px 0;
  background:linear-gradient(90deg,var(--brand-deep),#2a78c4)}
.brand-name{position:absolute;left:44px;top:0;line-height:66px;font-family:"Poppins",sans-serif;
  font-weight:600;font-size:31px;color:var(--white);white-space:nowrap}

.back-top{position:absolute;left:0;top:0;width:100%;height:250px;
  background:linear-gradient(180deg,var(--brand-mid) 0%,#2a78c2 55%,var(--brand-deep) 100%)}
.service-lines{position:absolute;left:0;top:101px;width:100%;text-align:center;
  font-family:"Roboto Condensed",sans-serif;font-style:italic;font-weight:700;font-size:23px;color:var(--white)}
.service-lines p{height:33px;line-height:33px;display:flex;justify-content:center;align-items:center;gap:22px}
.star{width:20px;height:20px;flex:none}

.back-quote{position:absolute;left:40px;right:40px;top:271px;text-align:center;
  font-family:"Noto Serif",serif;font-style:italic;font-size:15.5px;line-height:28px;color:var(--quote)}
.back-foot{position:absolute;left:0;bottom:0;width:100%;height:33px;background:var(--brand-deep)}
</style>
</head>
<body>

<header class="header-band">
  <div>Business Card - Mockup 2</div>
  <div>Rectangular CUT Available</div>
</header>

<section class="card card-front">
  <svg class="front-art" width="724" height="415" viewBox="0 0 724 415">
    <defs>
      <linearGradient id="solar-field" x1="0" y1="0" x2="0" y2="1">
        <stop offset="0" stop-color="#33b8ea"/>
        <stop offset=".32" stop-color="#3fc6f0"/>
        <stop offset=".42" stop-color="#2d5fb8"/>
        <stop offset=".66" stop-color="#1c3592"/>
        <stop offset=".82" stop-color="#3a6a78"/>
        <stop offset="1" stop-color="#4f8a3a"/>
      </linearGradient>
    </defs>
    <path d="M422 0 C346 110 350 280 520 415 L724 415 L724 0 Z" fill="#1f5cb0"/>
    <path d="M436 0 C372 110 380 278 538 415 L724 415 L724 0 Z" fill="#ffffff"/>
    <path d="M438 0 C378 112 386 276 544 415 L724 415 L724 0 Z" fill="url(#solar-field)"
          role="img" aria-label="Photo of solar panel array on grass under a blue sky"/>
  </svg>

  <h1 class="holder-name">Leo <strong>Harper</strong></h1>
  <p class="holder-role">Proprietor</p>

  <ul class="contact-list">
    <li>
      <svg class="contact-icon" viewBox="0 0 22 22"><circle cx="11" cy="11" r="11" fill="#2456a6"/>
        <path d="M7.5 6.5l2 -.3 1 2.3-1.2 1a6 6 0 0 0 3.2 3.2l1-1.2 2.3 1-.3 2c-4.5.4-8.4-3.5-8-8z" fill="#fff"/></svg>
      +12 4180 2736
    </li>
    <li>
      <svg class="contact-icon" viewBox="0 0 22 22"><circle cx="11" cy="11" r="11" fill="#2456a6"/>
        <rect x="6" y="7.5" width="10" height="7" rx="1" fill="none" stroke="#fff" stroke-width="1.4"/>
        <path d="M6.5 8.3l4.5 3.4 4.5-3.4" fill="none" stroke="#fff" stroke-width="1.4"/></svg>
      info@tvsolarco.com
    </li>
    <li>
      <svg class="contact-icon" viewBox="0 0 22 22"><circle cx="11" cy="11" r="11" fill="#2456a6"/>
        <circle cx="11" cy="11" r="5" fill="none" stroke="#fff" stroke-width="1.3"/>
        <ellipse cx="11" cy="11" rx="2.2" ry="5" fill="none" stroke="#fff" stroke-width="1.1"/>
        <path d="M6 11h10" stroke="#fff" stroke-width="1.1"/></svg>
      www.tvsolarco.com
    </li>
  </ul>

  <div class="brand-banner"><span class="brand-name">TV Solar Solution</span></div>
</section>

<section class="card card-back">
  <div class="back-top">
    <div class="service-lines">
      <p><span>Solar Power System Install</span>
        <svg class="star" viewBox="0 0 20 20"><path d="M10 2l2.4 5.2 5.6.6-4.2 3.8 1.2 5.6L10 14.4 5 17.2l1.2-5.6L2 7.8l5.6-.6z" fill="none" stroke="#fff" stroke-width="1.4" stroke-linejoin="round"/></svg>
        <span>Services &amp; Maintenance</span></p>
      <p><svg class="star" viewBox="0 0 20 20"><path d="M10 2l2.4 5.2 5.6.6-4.2 3.8 1.2 5.6L10 14.4 5 17.2l1.2-5.6L2 7.8l5.6-.6z" fill="none" stroke="#fff" stroke-width="1.4" stroke-linejoin="round"/></svg>
        <span>New wiring, Rewinding &amp; Renovation</span>
        <svg class="star" viewBox="0 0 20 20"><path d="M10 2l2.4 5.2 5.6.6-4.2 3.8 1.2 5.6L10 14.4 5 17.2l1.2-5.6L2 7.8l5.6-.6z" fill="none" stroke="#fff" stroke-width="1.4" stroke-linejoin="round"/></svg></p>
      <p><span>Switch Board Upgrade</span>
        <svg class="star" viewBox="0 0 20 20"><path d="M10 2l2.4 5.2 5.6.6-4.2 3.8 1.2 5.6L10 14.4 5 17.2l1.2-5.6L2 7.8l5.6-.6z" fill="none" stroke="#fff" stroke-width="1.4" stroke-linejoin="round"/></svg>
        <span>Power &amp; Lighting Point</span></p>
    </div>
  </div>
  <p class="back-quote">It doesn’t matter how much you spend on quality parts, your solar system will let you down if your design and installation are sub-par. Have your solar system tailored and installed by our Master Electrician and Bright Grid Guild Accredited team.</p>
  <div class="back-foot"></div>
</section>

</body>
</html>
```